Doctors Office Web Design

Name of the business is Lian-Hua Qiu M.D.
We need a web design that is attractive for women that want to see Dr. Lian-Hua Qiu for Obstetrician Gynecology and Pregnancy care. Dr. Qiu earned her degree from Harbor Crest Medical College of obstetrician gynecology. We want to attract women of child bearing ages to come to our offices for health, education, and pregnancies.

Please visit http://www.drqiucare-example.com/ to help you get a feel for who we are. We will be adding some pictures and logo in the next few days.

We are looking for to have pages for and tabs including
About Us- History, Our Staff, Dr. Qiu
Patient Information- Appointments, E-Prescriptions, Payments Accepted, Insurance
Health- General, Sexual, Mental, Affiliates
Pregnancy- Minimally invasive surgery(our specialty), 4-D Ultra Sound, Hospital Affiliations
Media- News,Pictures, Videos
Locations- Palmvale Office, Marlow Office

The colors we would like to use are pastel colors, magenta, and plum

Target Market(s)

Women of all ages with an emphasis on 25-65 year olds

Industry/Entity Type

Business

Requirements
Must have
• Needs to include a location for a our videos and pictures that I will submit shortly. We also want a map to our location or atleast a place for one.
Nice to have
• A place for a google map of our office locations.

```html
<!DOCTYPE html>
<html lang="en">
<head>
<meta charset="utf-8">
<title>Lian-Hua Qiu M.D. — Obstetrician/Gynecologist</title>
<link href="https://fonts.googleapis.com/css2?family=Questrial&family=Pinyon+Script&display=swap" rel="stylesheet">
<style>
:root{
  --sky:#cfdcef;
  --sky-deep:#9fb8de;
  --panel:#3566ad;
  --navy:#0f2a4d;
  --navy-2:#1b3a66;
  --card:#7ea6dc;
  --card-light:#8db1e2;
  --ink:#111;
  --white:#fff;
  --link-dark:#0c2447;
  --script-blue:#3b6db8;
}
*{box-sizing:border-box;margin:0;padding:0}
html,body{width:1200px;height:876px;overflow:hidden}
body{font-family:"Questrial",sans-serif;color:var(--ink);background:var(--white);position:relative}
.backdrop{position:absolute;left:0;top:5px;width:1200px;height:846px;
  background:radial-gradient(circle at 85% 25%,#e9f0fa 0,var(--sky) 45%,var(--sky-deep) 100%)}
.topline{position:absolute;left:0;top:0;width:1200px;height:5px;background:var(--sky-deep)}
.baby-photo{position:absolute;left:0;top:300px;width:175px;height:551px;
  background:radial-gradient(ellipse at 40% 45%,#a8c0e6 0,#8fadde 55%,#9cb6e0 100%);opacity:.8}
.logo{position:absolute;left:189px;top:12px;width:188px;height:58px;background:var(--card);
  display:flex;align-items:center;justify-content:center;font-size:20px;font-weight:700;letter-spacing:1px;color:var(--ink)}
.nav{position:absolute;left:384px;top:46px;display:flex;font-size:17px}
.nav a{color:var(--ink);text-decoration:none;padding:4px 8px 0;height:33px;margin-right:6px}
.nav a.current{background:var(--card);border-radius:8px 8px 0 0}
.panel{position:absolute;left:173px;top:92px;width:823px;height:759px;background:var(--panel);
  box-shadow:0 0 8px rgba(0,0,0,.3)}
.hero-frame{position:absolute;left:179px;top:74px;width:808px;height:285px;background:var(--navy);border-radius:12px}
.hero{position:absolute;left:190px;top:81px;width:784px;height:261px;background:var(--white);border-radius:0 0 10px 10px;overflow:hidden}
.hero-photo{position:absolute;left:330px;top:0;width:454px;height:261px;
  background:linear-gradient(90deg,#fff 0,#f1ddd2 25%,#e8c8b8 55%,#f3e2d9 80%,#fff 100%)}
.hero-copy{position:absolute;left:14px;top:66px}
.hero-script{font-family:"Pinyon Script",cursive;color:var(--script-blue);font-size:29px;line-height:31px}
.hero-script .cap{font-size:70px;line-height:50px;vertical-align:-14px}
.hero-script .l2{display:block;padding-left:80px}
.doctor{font-size:21px;margin-left:12px;margin-top:4px}
.specialty{font-size:21px;font-weight:700;margin-left:12px}
.dots{position:absolute;left:558px;top:345px;display:flex;gap:5px}
.dots span{width:10px;height:10px;border-radius:50%;background:var(--card-light)}
.services{position:absolute;left:196px;top:363px;font-size:14px;color:var(--white)}
.search{position:absolute;left:815px;top:364px;width:140px;height:15px;background:var(--navy);border-radius:7px;
  color:var(--white);font-size:12px;padding-left:7px;line-height:15px}
.search-icon{position:absolute;left:957px;top:365px}
.card-frame{position:absolute;width:260px;height:204px;background:var(--navy);border-radius:9px}
.card{position:absolute;width:246px;height:184px;background:var(--card);border-radius:6px;overflow:hidden}
.card-photo{position:absolute;left:0;top:0;width:246px;height:148px}
.card-caption{position:absolute;left:6px;top:151px;font-size:14px;line-height:16px;color:var(--ink)}
.card-caption .more{color:var(--link-dark)}
.welcome-title{position:absolute;left:0;top:-4px;font-family:"Pinyon Script",cursive;font-size:44px;color:var(--navy-2)}
.welcome-text{position:absolute;left:9px;top:54px;width:232px;font-size:10.5px;line-height:15.8px;color:var(--ink)}
.news-title{position:absolute;left:190px;top:596px;font-family:"Pinyon Script",cursive;font-size:46px;color:var(--white)}
.news-rule{position:absolute;left:193px;top:648px;width:505px;height:1px;background:#6d93cc}
.article-title{position:absolute;left:194px;top:654px;font-size:20px;font-weight:700;color:var(--navy);letter-spacing:.5px}
.article-body{position:absolute;left:194px;top:678px;width:510px;font-size:10.5px;line-height:15.8px;color:var(--white)}
.article-body .link{color:#cfdcef}
.meta{font-size:10.5px;color:#9fbbe3}
.meta b{font-weight:400;color:var(--link-dark)}
.more-news{position:absolute;left:194px;top:813px;font-size:12px;color:var(--white);text-decoration:underline}
.map-frame{position:absolute;left:728px;top:596px;width:259px;height:241px;background:var(--navy);border-radius:9px}
.map-card{position:absolute;left:735px;top:602px;width:245px;height:222px;background:var(--card);border-radius:6px;overflow:hidden}
.map{position:absolute;left:0;top:0;width:245px;height:189px;
  background:linear-gradient(135deg,#eeeae2 0,#e4ded2 50%,#efe9c2 100%)}
.map-caption{position:absolute;left:15px;top:198px;font-size:14.5px;color:var(--white)}
.map-caption span{color:var(--link-dark)}
.footer{position:absolute;left:0;top:851px;width:1200px;height:25px;background:var(--white);
  text-align:center;font-size:11px;line-height:25px;color:var(--ink)}
</style>
</head>
<body>
<div class="topline"></div>
<div class="backdrop"></div>
<div class="baby-photo" role="img" aria-label="Faint photo of a smiling baby"></div>

<div class="logo">LOGO</div>
<nav class="nav">
  <a class="current" href="#">home</a><a href="#">about</a><a href="#">patients info</a><a href="#">health</a><a href="#">pregnancy</a><a href="#">media</a><a href="#">locations</a>
</nav>

<div class="panel"></div>
<div class="hero-frame"></div>
<div class="hero">
  <div class="hero-photo" role="img" aria-label="Photo of a pregnant woman cradling her belly"></div>
  <div class="hero-copy">
    <div class="hero-script"><span class="cap">S</span>erving all areas<span class="l2">of women's health,</span></div>
    <div class="doctor">lian-hua qiu, m.d., facog</div>
    <div class="specialty">Obstetrician/Gynecologist</div>
  </div>
</div>
<div class="dots"><span></span><span></span><span></span><span></span></div>

<div class="services">Obstetrics, Family, Planning, Hormonal Evaluation, Incontinence, Infertility, and Gynecology</div>
<div class="search">search...</div>
<svg class="search-icon" width="14" height="14" viewBox="0 0 14 14"><circle cx="5" cy="5" r="3.5" fill="none" stroke="#9fbbe3" stroke-width="2"/><line x1="8" y1="8" x2="13" y2="13" stroke="#9fbbe3" stroke-width="2.5"/></svg>

<div class="card-frame" style="left:180px;top:385px"></div>
<div class="card" style="left:187px;top:392px">
  <div class="card-photo" role="img" aria-label="Photo of three smiling women" style="background:linear-gradient(135deg,#f3efe8,#d9c2a8 50%,#eef1f4)"></div>
  <div class="card-caption">Where can I find information on<br>living healthily? <span class="more">Nutrition »</span></div>
</div>

<div class="card-frame" style="left:455px;top:385px"></div>
<div class="card" style="left:462px;top:392px">
  <div class="welcome-title">Welcome</div>
  <p class="welcome-text">Here you will be able to find information about both of our offices, meet Dr. Qiu and her staff, and browse through our women's health links to learn more about pregnancy, nutrition, exercise, and other women's health issues. Have fun and if you have any questions, feel free to contact us at drqiu@harbormail-example.net</p>
</div>

<div class="card-frame" style="left:728px;top:385px"></div>
<div class="card" style="left:735px;top:392px">
  <div class="card-photo" role="img" aria-label="Photo of a newborn's hand holding a parent's finger" style="background:linear-gradient(135deg,#8a5a48,#d4a08a 50%,#b7c6dc)"></div>
  <div class="card-caption">Worried about breastfeeding?<br><span class="more">Post Pregnancy Concerns »</span></div>
</div>

<div class="news-title">News</div>
<div class="news-rule"></div>
<h2 class="article-title">Folic Acid Facts</h2>
<div class="article-body">
  <p>It is very important for women to get enough folic acid in their diet to prevent birth defects during pregnancy. Even young women who might not be planning to be a mother for five or ten years should already be making sure they are getting enough folic acid. All women and teenagers who could potentially become pregnant are at risk to have too low levels of folic acid cause certain neural birth defects. For more, please read this fact sheet.</p>
  <p class="link">Folic Acid Facts »</p>
  <p class="meta" style="margin-top:5px">Filed Under <b>FAQ</b> Tagged <b>nutrition</b>, <b>pregnancy</b>, <b>birth defects</b></p>
</div>
<a class="more-news" href="#">More News »</a>

<div class="map-frame"></div>
<div class="map-card">
  <div class="map" role="img" aria-label="Street map showing the office locations"></div>
  <div class="map-caption">Find Us at these Two <span>Locations</span> &nbsp;»</div>
</div>

<footer class="footer">home | about | contact | site map | disclaimer</footer>
</body>
</html>
```